Waterjet Cutting Business requires an up to date website

We currently have a website which is outdated and in need of modernization.
We are only looking for a simple website with around 4 pages: Home, Contact Us, Materials, Gallery.
We have some pictures and a logo which can be used.
Our primary business is profile cutting of materials to customers specifications using high-pressure water with abrasive.
We are looking for creative ideas and are open to suggestions!
http://brimfieldcutworks.com/index.asp?pid=1
Update:
Cut quality picture (uploaded)
Map
Comparison to other profile cutting methods such as plasma/laser
Single page style without continuous scrolling
"We can cut virtually any material from any drawing whether it be a Full 3D cad models to hand sketched "
Target Market(s)
Film Industry, Prototype, Engineering, Architect, Artisits, one off designs
Industry/Entity Type
Engineering
Number of Pages Required
1 page
Font styles to use
Look and feel

```html
<!DOCTYPE html>
<html lang="en">
<head>
<meta charset="utf-8">
<title>Brimfield Cutworks – Waterjet Profile Cutting</title>
<link rel="stylesheet" href="https://fonts.googleapis.com/css2?family=Orbitron:wght@700&family=Questrial&family=Arimo:wght@400;700&display=swap">
<style>
:root{
  --navy:#1a5a86;
  --nav-blue:#1d6694;
  --nav-active:#1b3850;
  --orange:#f06a18;
  --orange-dark:#d8520c;
  --ink:#3a3a3a;
  --paper:#efefee;
  --white:#ffffff;
  --field:rgba(78,78,78,.78);
}
*{margin:0;padding:0;box-sizing:border-box}
html,body{width:1200px;height:2473px;overflow:hidden}
body{position:relative;background:var(--white);font-family:"Questrial",sans-serif;color:var(--ink)}
.abs{position:absolute}

/* top bar */
.topbar{left:0;top:0;width:1200px;height:36px;background:var(--white);border-top:3px solid var(--navy)}
.contact-chip{top:6px;display:flex;align-items:center;gap:10px;font-size:13px;color:#333;font-family:"Arimo",sans-serif}
.contact-chip .ic{width:24px;height:24px;border:1.5px solid #333;border-radius:50%;display:flex;align-items:center;justify-content:center}
.contact-chip b{font-weight:400;color:var(--navy)}

/* nav */
.navbar{left:0;top:36px;width:1200px;height:37px;background:var(--nav-blue)}
.nav{left:414px;top:36px;height:37px;display:flex;font-family:"Arimo",sans-serif;font-size:12px;color:var(--white)}
.nav a{display:flex;align-items:center;justify-content:center;color:inherit;text-decoration:none;border-right:1px solid rgba(0,0,0,.25)}
.nav a.active{background:var(--nav-active)}
.logo-tab{left:140px;top:0;width:245px;height:84px}
.brand{left:188px;top:25px;display:flex;align-items:center;gap:10px;font-family:"Orbitron",sans-serif;font-weight:700;font-size:18px;color:var(--navy);letter-spacing:1px}
.brand i{width:14px;height:14px;border-radius:50%;background:var(--navy);display:block}

/* hero */
.hero{left:0;top:73px;width:1200px;height:504px;background:radial-gradient(ellipse at 72% 55%,#1f5e62 0%,#0f2b2e 28%,#050808 60%,#000 100%)}
.hero-title{left:143px;top:257px;width:480px;font-family:"Arimo",sans-serif;font-weight:400;font-size:25px;line-height:35px;color:var(--white)}
.dots{left:143px;top:419px;display:flex;gap:5px}
.dots span{width:11px;height:11px;border-radius:50%;background:#888;border:1.5px solid #ccc}
.dots span.on{background:var(--nav-blue)}

/* section titles */
.title{font-family:"Orbitron",sans-serif;font-weight:700;color:var(--navy);font-size:20px;letter-spacing:2px;text-align:center;width:1200px;left:0}
.title small{font-size:10px;letter-spacing:1px}
.rule{height:3px;width:54px;background:currentColor;border-radius:2px}

/* about */
.about{left:0;top:577px;width:1200px;height:412px;background:var(--paper)}
.about-copy{left:190px;top:718px;width:830px;text-align:center;font-size:12.5px;line-height:21.5px;color:#444}
.about-copy p+p{margin-top:2px}
.btn{display:flex;align-items:center;justify-content:center;gap:10px;height:32px;border-radius:16px;background:linear-gradient(var(--orange),var(--orange-dark));color:var(--white);font-family:"Orbitron",sans-serif;font-weight:700;font-size:9.5px;letter-spacing:.5px;text-decoration:none}
.btn i{width:20px;height:20px;border-radius:50%;background:var(--white);display:flex;align-items:center;justify-content:center}

/* materials */
.materials{left:0;top:989px;width:1200px;height:486px;background:linear-gradient(120deg,#16506f 0%,#1d6491 50%,#184f74 100%)}
.mat-frame{left:152px;top:1085px;width:346px;height:306px;background:#7fb9d8}
.mat-photo{left:142px;top:1075px;width:346px;height:306px;background:linear-gradient(150deg,#cfd8de 0%,#6d7f8e 35%,#2d3a44 70%,#101418 100%)}
.mat-title{left:531px;top:1072px;font-family:"Orbitron",sans-serif;font-weight:700;font-size:20px;letter-spacing:2px;color:var(--white)}
.mat-rule{left:531px;top:1104px;color:#cfe6f4}
.mat-copy{left:531px;top:1132px;width:526px;color:var(--white);font-size:12.5px;line-height:21px}
.mat-copy h3{font-weight:400;font-size:15.5px;margin-bottom:8px}
.mat-copy p{margin-bottom:10px}

/* gallery */
.gallery-title{top:1556px}
.gallery-rule{left:573px;top:1590px;color:var(--navy)}
.thumb{top:1625px;width:170px;height:199px;border:4px solid #ddd}
.thumb.teal{background:radial-gradient(circle at 55% 70%,#2fa89a,#0b2422 55%,#020303)}
.thumb.blue{background:linear-gradient(160deg,#3e7ec8,#1e4f9a)}
.thumb.cyan{background:radial-gradient(circle at 45% 40%,#3b8caa,#112433 60%,#05090c)}
.thumb.violet{background:radial-gradient(circle at 50% 45%,#c04aa0,#2a3a9e 45%,#0b1030)}
.thumb.green{background:radial-gradient(circle at 50% 55%,#35c24b,#0d4a17 55%,#031006)}
.thumb-over{position:absolute;inset:0;display:flex;flex-direction:column;align-items:center;justify-content:center;gap:10px;color:var(--white);font-family:"Arimo",sans-serif;font-weight:700;font-size:12px;text-align:center;line-height:16px;background:rgba(30,80,160,.55)}
.thumb-over i{width:32px;height:32px;border:2px solid var(--white);border-radius:50%;display:flex;align-items:center;justify-content:center;font-style:normal;font-size:22px;font-weight:400}
.arrow{top:1706px;width:37px;height:36px;display:flex;align-items:center;justify-content:center}
.arrow.prev{left:82px;background:#9a9a9a}
.arrow.next{left:1081px;background:var(--navy)}

/* inquiry */
.map{left:0;top:1912px;width:1200px;height:561px;background:linear-gradient(160deg,#d6d6d6,#c4c4c4 50%,#cdcdcd)}
.inq-title{top:1995px;color:#5b7286}
.inq-rule{left:573px;top:2028px;color:#5b7286}
.field{background:var(--field);color:var(--white);font-size:12px;display:flex;align-items:center;gap:12px;padding-left:12px}
.field .sep{width:1px;height:22px;background:rgba(255,255,255,.4)}
.field.msg{align-items:flex-start;padding-top:12px}
.pin-label{left:614px;top:2177px;font-size:11px;color:#a2231f;white-space:nowrap}
.info{top:2307px;height:99px;background:var(--field);color:var(--white);font-size:12.5px;line-height:17px;text-align:center;display:flex;flex-direction:column;align-items:center;justify-content:center;gap:6px}
.copyright{left:143px;top:2439px;font-size:11px;color:#333}
.social{top:2435px;display:flex;gap:6px;left:957px}
.social span{width:22px;height:22px;border-radius:50%;background:var(--navy)}
.zoom{left:1160px;top:2390px;width:22px;height:50px;background:var(--white);box-shadow:0 1px 3px rgba(0,0,0,.3)}
</style>
</head>
<body>

<header>
  <div class="abs topbar"></div>
  <div class="abs contact-chip" style="left:618px">
    <span class="ic"><svg width="12" height="12" viewBox="0 0 24 24"><path d="M6.6 10.8a15 15 0 0 0 6.6 6.6l2.2-2.2c.3-.3.7-.4 1-.2 1.1.4 2.3.6 3.6.6.6 0 1 .4 1 1V20c0 .6-.4 1-1 1A17 17 0 0 1 3 4c0-.6.4-1 1-1h3.5c.6 0 1 .4 1 1 0 1.3.2 2.5.6 3.6.1.3 0 .7-.2 1z" fill="#333"/></svg></span>
    <span>Call : <b>01632 960418</b></span>
  </div>
  <div class="abs contact-chip" style="left:818px">
    <span class="ic"><svg width="12" height="10" viewBox="0 0 24 18"><rect x="1" y="1" width="22" height="16" rx="2" fill="none" stroke="#333" stroke-width="2"/><path d="M1 2l11 8 11-8" fill="none" stroke="#333" stroke-width="2"/></svg></span>
    <span>email : <b>info@brimfieldcutworks.com</b></span>
  </div>

  <div class="abs navbar"></div>
  <svg class="abs logo-tab" viewBox="0 0 245 84" aria-hidden="true"><polygon points="0,0 245,0 225,84 20,84" fill="#fff"/></svg>
  <div class="abs brand"><i></i>BRIMFIELD</div>
  <nav class="abs nav">
    <a class="active" href="#" style="width:97px">home</a>
    <a href="#" style="width:129px">about us</a>
    <a href="#" style="width:145px">Materials</a>
    <a href="#" style="width:120px">Gallery</a>
    <a href="#" style="width:152px">Contact Us</a>
  </nav>
</header>

<section>
  <div class="abs hero" role="img" aria-label="Close-up photograph of a waterjet cutting head firing onto a glowing grid bed"></div>
  <h1 class="abs hero-title">Providing A Model Making And Profile Cutting of Materials To Customers Specifications Using High Pressure Water With Abrasive</h1>
  <div class="abs dots"><span class="on"></span><span></span><span></span></div>
</section>

<section>
  <div class="abs about"></div>
  <h2 class="abs title" style="top:657px">ABOUT BRIMFIELD <small>CUTWORKS</small></h2>
  <div class="abs about-copy">
    <p>Brimfield Cutworks is part of the Meridian Arts Group who have been providing a model making and profile cutting service primarily to the film industry for over 10 years. We are used to working within tight timeframes with a fast turnaround for all aspects of Water Jet Profiling, Tile Water Jet Cutting, Abrasive Steel Cutting and Foam Water Jet Cutting.</p>
    <p>By combining our technical expertise with Corvane's latest dynamic head waterjet technology we are able to offer a Profiling Services which can be tailored to each individual client and completed within fine tolerances to precise specifications. We are happy to cut your material or where required we can source most materials to your requirement.</p>
  </div>
  <a class="abs btn" href="#" style="left:532px;top:875px;width:134px">READ MORE <i><svg width="8" height="10" viewBox="0 0 8 10"><path d="M2 1l4 4-4 4" fill="none" stroke="#e85f12" stroke-width="2"/></svg></i></a>
</section>

<section>
  <div class="abs materials"></div>
  <div class="abs mat-frame"></div>
  <div class="abs mat-photo" role="img" aria-label="Photograph of a waterjet cutting head over a metal slat bed"></div>
  <h2 class="abs mat-title">MATERIALS</h2>
  <div class="abs rule mat-rule"></div>
  <div class="abs mat-copy">
    <h3>It is possible to cut virtually any profile in any material with waterjet</h3>
    <p>Materials we can cut include, but are not limited to, all metals &amp; alloys, stone and ceramics, composites, solid-surface sheet, wood, glass, acrylics, resins, silicones, plastics, foams, carpet &amp; felts. We can also cut laminated dissimilar materials which can often be very hard to cut using conventional methods. We are always happy to test cut a sample of your material free of charge to demonstrate the quality of cut achievable.</p>
    <p>Employing Corvane's low pressure vacuum assist we can pierce and cut brittle materials such as acrylics &amp; ceramics. In addition Corvane Vectra head technology with Live Taper Control produces more accurate parts at significantly higher cutting speeds than parts cut with a conventional waterjet.</p>
    <p>If you are not sure whether waterjet cutting will fulfill your requirements give us a call.</p>
  </div>
</section>

<section>
  <h2 class="abs title gallery-title">PHOTO GALLERY</h2>
  <div class="abs rule gallery-rule"></div>
  <div class="abs arrow prev"><svg width="16" height="10" viewBox="0 0 16 10"><path d="M15 5H2M6 1L2 5l4 4" fill="none" stroke="#fff" stroke-width="2"/></svg></div>
  <div class="abs thumb teal" style="left:143px" role="img" aria-label="Waterjet nozzle with teal lighting"></div>
  <div class="abs thumb blue" style="left:329px" role="img" aria-label="Cutting machine in blue light">
    <div class="thumb-over"><i>+</i>Lorem ipsum dolor amet<br>consectr adipiscing</div>
  </div>
  <div class="abs thumb cyan" style="left:514px" role="img" aria-label="Waterjet head assembly"></div>
  <div class="abs thumb violet" style="left:700px" role="img" aria-label="Cutting head under violet and red light"></div>
  <div class="abs thumb green" style="left:885px" role="img" aria-label="Cutting head under green light"></div>
  <div class="abs arrow next"><svg width="16" height="10" viewBox="0 0 16 10"><path d="M1 5h13M10 1l4 4-4 4" fill="none" stroke="#fff" stroke-width="2"/></svg></div>
</section>

<section>
  <div class="abs map" role="img" aria-label="Street map showing the workshop location"></div>
  <h2 class="abs title inq-title">QUICK INQUIRY</h2>
  <div class="abs rule inq-rule"></div>

  <div class="abs field" style="left:143px;top:2065px;width:292px;height:41px">
    <svg width="13" height="13" viewBox="0 0 24 24"><circle cx="12" cy="7" r="5" fill="#fff"/><path d="M2 23c0-6 4-9 10-9s10 3 10 9z" fill="#fff"/></svg><span class="sep"></span>Name</div>
  <div class="abs field" style="left:454px;top:2065px;width:292px;height:41px">
    <svg width="13" height="13" viewBox="0 0 24 24"><path d="M6.6 10.8a15 15 0 0 0 6.6 6.6l2.2-2.2c.3-.3.7-.4 1-.2 1.1.4 2.3.6 3.6.6.6 0 1 .4 1 1V20c0 .6-.4 1-1 1A17 17 0 0 1 3 4c0-.6.4-1 1-1h3.5c.6 0 1 .4 1 1 0 1.3.2 2.5.6 3.6.1.3 0 .7-.2 1z" fill="#fff"/></svg><span class="sep"></span>Phone</div>
  <div class="abs field" style="left:765px;top:2065px;width:293px;height:41px">
    <svg width="14" height="11" viewBox="0 0 24 18"><rect x="1" y="1" width="22" height="16" rx="2" fill="none" stroke="#fff" stroke-width="2"/><path d="M1 2l11 8 11-8" fill="none" stroke="#fff" stroke-width="2"/></svg><span class="sep"></span>Email</div>
  <div class="abs field msg" style="left:143px;top:2129px;width:915px;height:106px">
    <svg width="14" height="13" viewBox="0 0 24 22"><path d="M2 2h20v14H9l-5 4v-4H2z" fill="#fff"/></svg><span class="sep"></span>Message</div>

  <svg class="abs" style="left:588px;top:2165px" width="24" height="34" viewBox="0 0 24 34" aria-hidden="true"><path d="M12 33C12 33 1 19 1 12a11 11 0 0 1 22 0c0 7-11 21-11 21z" fill="#c9302c"/><circle cx="12" cy="12" r="4" fill="#7a1613"/></svg>
  <span class="abs pin-label">Brimfield Cutworks</span>

  <a class="abs btn" href="#" style="left:531px;top:2258px;width:136px">SUBMIT NOW <i><svg width="8" height="10" viewBox="0 0 8 10"><path d="M2 1l4 4-4 4" fill="none" stroke="#e85f12" stroke-width="2"/></svg></i></a>

  <div class="abs info" style="left:234px;width:227px">
    <svg width="14" height="18" viewBox="0 0 24 32"><path d="M12 30S3 18 3 11a9 9 0 0 1 18 0c0 7-9 19-9 19z" fill="none" stroke="#fff" stroke-width="2"/><circle cx="12" cy="11" r="3" fill="none" stroke="#fff" stroke-width="2"/></svg>
    <span>Unit 7, Brook Park, Mill Rd,<br>Brimfield BF4 2TX, UK</span></div>
  <div class="abs info" style="left:476px;width:226px">
    <svg width="16" height="16" viewBox="0 0 24 24"><path d="M6.6 10.8a15 15 0 0 0 6.6 6.6l2.2-2.2c.3-.3.7-.4 1-.2 1.1.4 2.3.6 3.6.6.6 0 1 .4 1 1V20c0 .6-.4 1-1 1A17 17 0 0 1 3 4c0-.6.4-1 1-1h3.5c.6 0 1 .4 1 1 0 1.3.2 2.5.6 3.6.1.3 0 .7-.2 1z" fill="none" stroke="#fff" stroke-width="1.6"/></svg>
    <span>Call:<br>01632 960418</span></div>
  <div class="abs info" style="left:719px;width:225px">
    <svg width="18" height="14" viewBox="0 0 24 18"><rect x="1" y="1" width="22" height="16" rx="2" fill="none" stroke="#fff" stroke-width="2"/><path d="M1 2l11 8 11-8" fill="none" stroke="#fff" stroke-width="2"/></svg>
    <span>Email:<br>info@brimfieldcutworks.com</span></div>

  <div class="abs zoom"></div>
  <p class="abs copyright">Copyright © 2018 Brimfield Cutworks. All Rights Reserved</p>
  <div class="abs social"><span></span><span></span><span></span><span></span></div>
</section>

</body>
</html>
```